Business Card Design Project

it should have the logo in one side
the other side

Name
Position
telephone
email

Target Market(s)

Business prospects and upscale Fashion shoppers

Industry/Entity Type

Business

Font styles to use
Serif
Sans Serif

Requirements
Must have
• very elegant, upscale, modern
Nice to have
• layering, embossed
Should not have
• Should not use any color OTHER THAN black, silver, white or purple

```html
<!DOCTYPE html>
<html lang="en">
<head>
<meta charset="utf-8">
<title>Velora Business Card</title>
<link rel="stylesheet" href="https://fonts.googleapis.com/css2?family=Josefin+Sans:wght@300&family=Open+Sans:wght@400;600;700&display=swap">
<style>
  :root {
    --backdrop: #a9a9a9;
    --card-white: #ffffff;
    --ink: #111111;
    --purple: #8e44a4;
    --purple-light: #8a4a9c;
    --purple-deep: #6d2a86;
    --purple-emboss: #5c1f72;
    --rule: #222222;
  }
  * { box-sizing: border-box; margin: 0; padding: 0; }
  html, body {
    width: 1200px;
    height: 900px;
    overflow: hidden;
    background: var(--backdrop);
  }
  .stage {
    width: 1200px;
    height: 900px;
    display: flex;
    align-items: center;
    justify-content: center;
    gap: 60px;
  }
  .card {
    position: relative;
    width: 525px;
    height: 300px;
    box-shadow: 0 10px 24px rgba(0, 0, 0, 0.25);
    overflow: hidden;
  }

  /* Front: contact side */
  .card-front { background: var(--card-white); }
  .front-brand {
    position: absolute;
    top: 62px;
    left: 160px;
    display: flex;
    align-items: center;
    gap: 12px;
  }
  .brand-square {
    width: 16px;
    height: 16px;
    background: var(--purple);
  }
  .brand-name {
    font-family: "Josefin Sans", sans-serif;
    font-weight: 300;
    font-size: 46px;
    letter-spacing: 2px;
    color: var(--ink);
    line-height: 1;
  }
  .person {
    position: absolute;
    top: 168px;
    left: 190px;
    text-align: center;
    font-family: "Open Sans", sans-serif;
  }
  .person-name {
    font-size: 18px;
    font-weight: 600;
    color: var(--purple);
    letter-spacing: -0.3px;
  }
  .person-role {
    font-size: 14px;
    font-weight: 700;
    color: var(--ink);
    margin-top: -2px;
  }
  .divider {
    position: absolute;
    left: 24px;
    right: 24px;
    top: 224px;
    height: 1px;
    background: var(--rule);
  }
  .contact {
    position: absolute;
    display: flex;
    align-items: center;
    gap: 8px;
    font-family: "Open Sans", sans-serif;
    color: var(--ink);
  }
  .contact-phone { left: 24px; top: 240px; font-size: 14px; }
  .contact-email { right: 26px; top: 254px; font-size: 16px; font-weight: 600; }
  .contact svg { fill: var(--purple); display: block; }

  /* Back: brand side */
  .card-back {
    background: linear-gradient(180deg, var(--purple-light) 0%, var(--purple-deep) 100%);
  }
  .back-brand {
    position: absolute;
    right: 40px;
    bottom: 70px;
    display: flex;
    align-items: center;
    gap: 12px;
  }
  .back-brand .brand-square {
    width: 18px;
    height: 18px;
    background: var(--purple-emboss);
    box-shadow: 1px 1px 0 rgba(255, 255, 255, 0.18);
  }
  .back-brand .brand-name {
    font-size: 52px;
    color: var(--purple-emboss);
    text-shadow: 1px 1px 0 rgba(255, 255, 255, 0.18);
  }
</style>
</head>
<body>
<main class="stage">
  <section class="card card-front" aria-label="Card front">
    <div class="front-brand">
      <span class="brand-square"></span>
      <span class="brand-name">VELORA</span>
    </div>
    <div class="person">
      <p class="person-name">YOUR NAMME</p>
      <p class="person-role">DSIGNATION</p>
    </div>
    <div class="divider"></div>
    <p class="contact contact-phone">
      <svg width="15" height="12" viewBox="0 0 15 12" aria-hidden="true">
        <path d="M1 4 Q7.5 -1 14 4 L12 6 L10 4.5 L10 3 Q7.5 2 5 3 L5 4.5 L3 6 Z"/>
        <rect x="3" y="6" width="9" height="6" rx="1"/>
      </svg>
      <span>01632 960 482</span>
    </p>
    <p class="contact contact-email">
      <svg width="16" height="11" viewBox="0 0 16 11" aria-hidden="true">
        <path d="M0 0 H16 V11 H0 Z M1 1 L8 6.5 L15 1 Z" fill-rule="evenodd"/>
      </svg>
      <span>hello@velorastudio.com</span>
    </p>
  </section>

  <section class="card card-back" aria-label="Card back">
    <div class="back-brand">
      <span class="brand-square"></span>
      <span class="brand-name">VELORA</span>
    </div>
  </section>
</main>
</body>
</html>
```